Labels for Bees Wax Candles & Honey Jars

We need labels for jars of natural honey. Most of our jars are square and the labels about 2" by 2".

Also we make bees wax candles of various sizes. We wish to wrap th enables around the circular candles which are between 2" and 3" in diameter... thus another have inch per label so they can be attached adhesively. The candles also vary in height... therefor th enables need to be 1.5", 2" and 3" in height.

We ar elooking for a very artistic and simple label that may include vibrant colors.
The name of our company must be displayed.. Candles by Morrow and for the Honey.... Morrow's All Natural Honey
Updates

The labels will be used for both Honey Jars as well as Bees Wax candles. There will be various sizes but that is something that can be adjusted after the initial design is approved. The Honey Jars should read "Natural Honey by Morrow" and the Candle labels should read "Natural Bees Wax Candles by Morrow" I am interested in simple, colorful, legible, and arty labels that pertain to bees and the natural environment. Hope this helps. We may also use a similar design on our web page. The size of the label on the honey will be 2" by 2" and the candles will vary.

Target Market(s)

Individual that purchase natural and organic products.

Requirements
Must have
• Labels should be very creative but legible and the emphasis on the candles should be all natural bees wax and the emphasis on the honey should be all natural honey. We are talking about the same design but different sizes and names.
Nice to have
• brillant colors and artistic

```html
<!DOCTYPE html>
<html lang="en">
<head>
<meta charset="utf-8">
<title>Natural Honey &amp; Bees Wax Candles by Morrow — Labels</title>
<link rel="stylesheet" href="https://fonts.googleapis.com/css2?family=Crimson+Text:wght@400;600;700&display=swap">
<style>
  :root {
    --canvas: #ffffff;
    --leaf: #cddc2a;
    --sun: #ece41e;
    --tagline: #e3e64a;
    --comb: #f5901f;
    --title: #4b4a9c;
    --maker: #e4232b;
    --wax: #f1e23a;
    --dot: #ffffff;
  }
  * { margin: 0; padding: 0; box-sizing: border-box; }
  html, body { width: 1200px; height: 1000px; overflow: hidden; background: var(--canvas); }
  .sheet { position: relative; width: 1200px; height: 1000px; }

  .label { position: absolute; overflow: hidden; background: var(--leaf); font-family: "Crimson Text", Georgia, serif; }
  .label svg.art { position: absolute; inset: 0; }
  .label--honey   { left: 460px; top: 78px;  width: 283px; height: 282px; }
  .label--small   { left: 88px;  top: 443px; width: 283px; height: 213px; }
  .label--medium  { left: 460px; top: 443px; width: 284px; height: 285px; }
  .label--tall    { left: 832px; top: 444px; width: 284px; height: 426px; }

  .title, .maker, .tagline, .wax { position: absolute; white-space: nowrap; line-height: 1; }
  .title { color: var(--title); font-weight: 700; letter-spacing: 0.01em; }
  .maker { color: var(--maker); font-weight: 400; }
  .tagline { color: var(--tagline); right: var(--r); text-align: right; letter-spacing: 0.05em; }
  .wax { color: var(--wax); font-weight: 700; transform-origin: left bottom; }
  .wax--down { transform: rotate(45deg); }
  .wax--up { transform: rotate(-35deg); letter-spacing: 0.04em; }
</style>
</head>
<body>
<main class="sheet">

  <!-- Honey jar label -->
  <section class="label label--honey">
    <svg class="art" viewBox="0 0 283 282" width="283" height="282">
      <defs>
        <linearGradient id="band-b1" x1="0" y1="0" x2="0" y2="1"><stop offset="0" stop-color="#ece41e" stop-opacity="0"/><stop offset=".6" stop-color="#ece41e"/></linearGradient>
        <linearGradient id="band-r1" x1="0" y1="0" x2="1" y2="0"><stop offset="0" stop-color="#ece41e" stop-opacity="0"/><stop offset=".7" stop-color="#ece41e"/></linearGradient>
        <linearGradient id="bee-g" x1="0" y1="0" x2="1" y2="1"><stop offset="0" stop-color="#e9d632"/><stop offset=".5" stop-color="#4a2a12"/><stop offset="1" stop-color="#c9b52a"/></linearGradient>
      </defs>
      <rect x="0" y="244" width="283" height="38" fill="url(#band-b1)"/>
      <rect x="248" y="120" width="35" height="162" fill="url(#band-r1)"/>
      <polygon role="img" aria-label="Honeycomb pattern" fill="#f5901f" points="0,0 248,0 248,35 238,58 200,58 190,82 150,82 140,108 118,108 108,145 52,145 42,165 0,165"/>
      <rect role="img" aria-label="Illustration of a honey bee" x="0" y="95" width="92" height="125" rx="30" fill="url(#bee-g)"/>
      <circle cx="262" cy="133" r="8" fill="#fff"/>
      <circle cx="50" cy="258" r="8" fill="#fff"/>
    </svg>
    <h1 class="title" style="left:28px;top:48px;font-size:35px">Natural Honey</h1>
    <p class="maker" style="right:26px;top:81px;font-size:26px">by Morrow</p>
    <p class="tagline" style="--r:46px;top:140px;font-size:11px">all natural honey</p>
    <p class="tagline" style="--r:46px;top:155px;font-size:12px">all natural honey</p>
    <p class="tagline" style="--r:46px;top:172px;font-size:15px">all natural honey</p>
    <p class="tagline" style="--r:46px;top:194px;font-size:18px">all natural honey</p>
    <p class="tagline" style="--r:46px;top:218px;font-size:21px">all natural honey</p>
  </section>

  <!-- Candle label, short -->
  <section class="label label--small">
    <svg class="art" viewBox="0 0 283 213" width="283" height="213">
      <rect x="0" y="180" width="283" height="33" fill="url(#band-b1)"/>
      <rect x="250" y="70" width="33" height="143" fill="url(#band-r1)"/>
      <polygon role="img" aria-label="Honeycomb pattern" fill="#f5901f" points="0,0 225,0 225,25 215,45 180,45 172,70 150,70 142,95 120,95 110,125 105,150 60,150 0,150"/>
      <rect role="img" aria-label="Illustration of a honey bee" x="0" y="62" width="76" height="112" rx="26" fill="url(#bee-g)"/>
      <circle cx="264" cy="85" r="7" fill="#fff"/>
      <circle cx="82" cy="193" r="7" fill="#fff"/>
    </svg>
    <span class="wax wax--down" style="left:86px;top:-4px;font-size:18px">Bees</span>
    <span class="wax wax--up" style="left:125px;top:26px;font-size:18px">Wax</span>
    <h1 class="title" style="left:16px;top:42px;font-size:25px">Natural</h1>
    <h1 class="title" style="left:168px;top:40px;font-size:25px">Candles</h1>
    <p class="maker" style="right:18px;top:61px;font-size:18px">by Morrow</p>
    <p class="tagline" style="--r:36px;top:92px;font-size:8px">all natural honey</p>
    <p class="tagline" style="--r:36px;top:104px;font-size:9px">all natural honey</p>
    <p class="tagline" style="--r:36px;top:118px;font-size:12px">all natural honey</p>
    <p class="tagline" style="--r:36px;top:137px;font-size:14px">all natural honey</p>
    <p class="tagline" style="--r:36px;top:158px;font-size:17px">all natural honey</p>
  </section>

  <!-- Candle label, medium -->
  <section class="label label--medium">
    <svg class="art" viewBox="0 0 284 285" width="284" height="285">
      <rect x="0" y="246" width="284" height="39" fill="url(#band-b1)"/>
      <rect x="250" y="110" width="34" height="175" fill="url(#band-r1)"/>
      <polygon role="img" aria-label="Honeycomb pattern" fill="#f5901f" points="0,0 228,0 228,30 218,55 185,55 176,85 150,85 140,115 118,115 108,150 98,175 60,175 48,200 0,200"/>
      <rect role="img" aria-label="Illustration of a honey bee" x="0" y="82" width="98" height="140" rx="32" fill="url(#bee-g)"/>
      <circle cx="263" cy="132" r="8" fill="#fff"/>
      <circle cx="52" cy="258" r="8" fill="#fff"/>
    </svg>
    <span class="wax wax--down" style="left:96px;top:4px;font-size:20px">Bees</span>
    <span class="wax wax--up" style="left:138px;top:38px;font-size:20px">Wax</span>
    <h1 class="title" style="left:22px;top:60px;font-size:26px">Natural</h1>
    <h1 class="title" style="left:174px;top:58px;font-size:26px">Candles</h1>
    <p class="maker" style="right:14px;top:79px;font-size:19px">by Morrow</p>
    <p class="tagline" style="--r:38px;top:141px;font-size:10px">all natural honey</p>
    <p class="tagline" style="--r:38px;top:156px;font-size:11px">all natural honey</p>
    <p class="tagline" style="--r:38px;top:173px;font-size:14px">all natural honey</p>
    <p class="tagline" style="--r:38px;top:195px;font-size:17px">all natural honey</p>
    <p class="tagline" style="--r:38px;top:220px;font-size:20px">all natural honey</p>
  </section>

  <!-- Candle label, tall -->
  <section class="label label--tall">
    <svg class="art" viewBox="0 0 284 426" width="284" height="426">
      <rect x="0" y="385" width="284" height="41" fill="url(#band-b1)"/>
      <rect x="250" y="250" width="34" height="176" fill="url(#band-r1)"/>
      <polygon role="img" aria-label="Honeycomb pattern" fill="#f5901f" points="0,0 228,0 228,45 218,70 185,70 176,100 150,100 140,130 118,130 108,165 98,200 80,200 70,230 40,230 30,252 0,252"/>
      <rect role="img" aria-label="Illustration of a honey bee" x="0" y="128" width="94" height="132" rx="30" fill="url(#bee-g)"/>
      <circle cx="263" cy="269" r="8" fill="#fff"/>
      <circle cx="51" cy="396" r="8" fill="#fff"/>
    </svg>
    <span class="wax wax--down" style="left:94px;top:42px;font-size:20px">Bees</span>
    <span class="wax wax--up" style="left:136px;top:76px;font-size:20px">Wax</span>
    <h1 class="title" style="left:18px;top:97px;font-size:26px">Natural</h1>
    <h1 class="title" style="left:170px;top:96px;font-size:26px">Candles</h1>
    <p class="maker" style="right:16px;top:116px;font-size:19px">by Morrow</p>
    <p class="tagline" style="--r:39px;top:278px;font-size:10px">all natural honey</p>
    <p class="tagline" style="--r:39px;top:293px;font-size:11px">all natural honey</p>
    <p class="tagline" style="--r:39px;top:310px;font-size:14px">all natural honey</p>
    <p class="tagline" style="--r:39px;top:333px;font-size:17px">all natural honey</p>
    <p class="tagline" style="--r:39px;top:358px;font-size:20px">all natural honey</p>
  </section>

</main>
</body>
</html>
```